Beauty Clinic Treatment Menu (Lumen Nails & Beauty)

Needing a treatment menu designed for a beauty clinic in Ashmere Bay, New Zealand. Like the colours grey, pink, white.
Elegant, Modern and feminine

Lumen Nails & Beauty
Dana Pirrett
Suite 2, 17 Corbel Street
Ashmere Bay
0271836042
Dana.lumen@mailbay.example
lumenbeauty.example.nz

Target Market(s)

Females

Industry/Entity Type

Beauty Salon

Font styles to use
Serif

Colors

Designer to choose colors to be used in the design.

Requirements
Must have
• Chatterbook and Snapgrid logo

```html
<!DOCTYPE html>
<html lang="en">
<head>
<meta charset="utf-8">
<title>Lumen Nails &amp; Beauty – Treatment Menu</title>
<link rel="stylesheet" href="https://fonts.googleapis.com/css2?family=Playfair+Display:ital,wght@0,400;0,600;1,400&family=Lora:ital,wght@0,400;0,500;1,400&family=Questrial&family=Great+Vibes&display=swap">
<style>
  :root{
    --stage:#e3e3e4;
    --grey:#5e5c61;
    --grey-dark:#4d4b50;
    --rose:#c8927c;
    --rose-light:#e8c6ba;
    --blush:#f3e1db;
    --white:#ffffff;
    --ink:#4a4749;
    --muted:#8a8588;
  }
  *{box-sizing:border-box;margin:0;padding:0}
  html,body{width:1200px;height:2402px;overflow:hidden}
  body{background:var(--stage);font-family:"Lora",Georgia,serif;color:var(--ink);position:relative}

  .sheet{position:absolute;display:flex;box-shadow:0 18px 40px rgba(0,0,0,.18)}
  .sheet--cover{left:415px;top:40px}
  .sheet--outside{left:45px;top:820px}
  .sheet--inside{left:45px;top:1620px}

  .panel{position:relative;width:370px;height:740px;overflow:hidden;background:var(--white)}
  .panel + .panel{border-left:1px solid rgba(0,0,0,.06)}
  .layer{position:absolute;inset:0;width:370px;height:740px}

  .brand{position:absolute;left:0;right:0;text-align:center;font-family:"Playfair Display",Georgia,serif;color:var(--rose)}
  .brand__name{font-size:40px;line-height:1;letter-spacing:1px}
  .brand__sub{font-size:11px;letter-spacing:2px;margin-top:6px;color:var(--muted)}
  .brand--ring{top:60px;left:50%;width:120px;height:120px;margin-left:-60px;border:2px solid var(--rose);border-radius:50%;display:flex;flex-direction:column;align-items:center;justify-content:center}
  .brand--ring .brand__name{font-size:30px}
  .brand--ring .brand__sub{font-size:8px;letter-spacing:1px;margin-top:4px}

  .cover__title{position:absolute;left:0;right:0;top:596px;text-align:center;font-family:"Questrial",Arial,sans-serif;font-weight:400;font-size:36px;color:var(--rose)}
  .url-pill{position:absolute;left:50%;transform:translateX(-50%);border:1.5px solid var(--rose-light);border-radius:20px;padding:6px 22px;font-family:"Questrial",Arial,sans-serif;font-size:14px;color:var(--white);letter-spacing:.5px;white-space:nowrap}
  .cover .url-pill{top:660px}

  .about{position:absolute;left:32px;right:32px;top:40px}
  .heading{font-family:"Playfair Display",Georgia,serif;font-style:italic;font-weight:400;color:var(--rose);font-size:26px;margin-bottom:14px}
  .about p{font-size:11.5px;line-height:1.65;font-style:italic;margin-bottom:12px}

  .quote{position:absolute;left:36px;right:36px;top:210px;text-align:center}
  .quote__mark{font-family:"Playfair Display",Georgia,serif;color:var(--rose);font-size:44px;line-height:.6}
  .quote p{font-size:11.5px;line-height:1.6;font-style:italic;margin-top:10px}
  .call{position:absolute;left:0;right:0;top:330px;text-align:center}
  .call__script{font-family:"Great Vibes",cursive;font-size:40px;color:var(--rose);line-height:1}
  .call__phone{display:inline-flex;align-items:center;gap:8px;margin-top:10px;border:1.5px solid var(--rose-light);border-radius:18px;padding:4px 16px;font-family:"Questrial",Arial,sans-serif;font-size:15px;color:var(--ink)}
  .call__mail{margin-top:10px;font-family:"Questrial",Arial,sans-serif;font-size:12.5px;color:var(--rose)}
  .address{position:absolute;left:0;right:0;top:545px;text-align:center;color:var(--white);font-family:"Questrial",Arial,sans-serif;font-style:normal;font-size:15px;line-height:1.45}
  .socials{position:absolute;left:0;right:0;top:640px;display:flex;justify-content:center;gap:20px;font-family:"Questrial",Arial,sans-serif;font-size:12px;color:var(--white)}
  .social{display:flex;align-items:center;gap:6px}
  .social__dot{width:14px;height:14px;border-radius:50%;background:var(--rose)}
  .contact .url-pill{top:680px}

  .menu{position:absolute;left:30px;right:30px}
  .menu--nails{top:32px;color:var(--white)}
  .menu--facials{top:200px}
  .menu--face{top:470px;color:var(--white)}
  .menu__title{font-family:"Playfair Display",Georgia,serif;font-style:italic;font-weight:400;color:var(--rose);font-size:22px;margin-bottom:6px}
  .menu__group{font-family:"Questrial",Arial,sans-serif;font-size:10.5px;letter-spacing:1.5px;color:var(--rose-light);text-transform:uppercase;margin:10px 0 3px}
  .menu--facials .menu__group{color:var(--rose);letter-spacing:.5px;text-transform:none;font-size:12px}
  .row{display:flex;align-items:baseline;font-size:11.5px;line-height:1.55}
  .row__name{white-space:nowrap}
  .row__dots{flex:1;border-bottom:1px dotted currentColor;opacity:.55;margin:0 5px;transform:translateY(-3px)}
  .row__price{white-space:nowrap}
  .note{font-size:9.5px;font-style:italic;opacity:.85;line-height:1.35;margin-bottom:2px}
  .menu--facials .note{color:var(--muted)}
  .cols{display:flex;gap:26px}
  .cols > div{flex:1}
</style>
</head>
<body>

<section class="sheet sheet--cover">
  <article class="panel cover">
    <svg class="layer" viewBox="0 0 370 740" role="img" aria-label="Portrait photo of a model with long wavy hair and purple manicured nails">
      <defs><linearGradient id="coverPhoto" x1="0" y1="0" x2="1" y2="1"><stop offset="0" stop-color="#8a6a55"/><stop offset=".5" stop-color="#e2bfae"/><stop offset="1" stop-color="#6b4b45"/></linearGradient></defs>
      <path d="M0 95 Q185 150 370 95 L370 440 Q210 530 0 610 Z" fill="url(#coverPhoto)"/>
    </svg>
    <svg class="layer" viewBox="0 0 370 740" aria-hidden="true">
      <path d="M0 95 Q185 150 370 95" fill="none" stroke="var(--rose-light)" stroke-width="4"/>
      <path d="M0 606 Q210 526 370 436" fill="none" stroke="var(--blush)" stroke-width="8"/>
      <path d="M0 614 Q210 536 370 446" fill="none" stroke="var(--rose)" stroke-width="4"/>
      <path d="M0 620 Q210 542 370 452 L370 740 L0 740 Z" fill="var(--grey)"/>
    </svg>
    <div class="brand" style="top:20px"><div class="brand__name">Lumen</div><div class="brand__sub">Nails &amp; Beauty</div></div>
    <h1 class="cover__title">Nails &amp; Beauty</h1>
    <div class="url-pill">www.lumenbeauty.example.nz</div>
  </article>
</section>

<section class="sheet sheet--outside">
  <article class="panel about-panel">
    <svg class="layer" viewBox="0 0 370 740" role="img" aria-label="Photo montage of manicure and facial treatments">
      <defs><linearGradient id="aboutPhoto" x1="0" y1="0" x2="1" y2="1"><stop offset="0" stop-color="#e9d4cc"/><stop offset="1" stop-color="#b88f80"/></linearGradient></defs>
      <path d="M0 450 Q160 450 250 550 Q310 630 370 740 L0 740 Z" fill="url(#aboutPhoto)"/>
    </svg>
    <svg class="layer" viewBox="0 0 370 740" aria-hidden="true">
      <path d="M0 450 Q160 450 250 550 Q310 630 370 740" fill="none" stroke="var(--rose-light)" stroke-width="4"/>
    </svg>
    <div class="about">
      <h2 class="heading">About us</h2>
      <p>Lumen Nails &amp; Beauty is a modern salon in the heart of Ashmere Bay, offering a calm space to relax and be pampered. We offer manicures, pedicures, facials, waxing and lash and brow treatments, all tailored to you.</p>
      <p>We use gentle, quality products and take time to listen, so every visit leaves you feeling refreshed and confident. Book ahead or drop in and ask about our seasonal offers for new clients.</p>
    </div>
  </article>

  <article class="panel contact">
    <svg class="layer" viewBox="0 0 370 740" aria-hidden="true">
      <path d="M0 20 Q185 0 370 20" fill="none" stroke="var(--rose-light)" stroke-width="4"/>
      <path d="M0 470 Q185 525 370 470" fill="none" stroke="var(--rose)" stroke-width="4"/>
      <path d="M0 480 Q185 535 370 480 L370 740 L0 740 Z" fill="var(--grey)"/>
    </svg>
    <div class="brand brand--ring"><div class="brand__name">Lumen</div><div class="brand__sub">Nails &amp; Beauty</div></div>
    <div class="quote">
      <div class="quote__mark">&ldquo;</div>
      <p>I absolutely loved every single minute of my facial with Dana. I left the salon feeling so relaxed and my skin smooth and glowing. I can't wait for my next appointment!</p>
    </div>
    <div class="call">
      <div class="call__script">call us today</div>
      <div class="call__phone">
        <svg width="14" height="14" viewBox="0 0 24 24" aria-hidden="true"><path d="M6.6 10.8a15.1 15.1 0 0 0 6.6 6.6l2.2-2.2a1 1 0 0 1 1-.25 11.4 11.4 0 0 0 3.6.57 1 1 0 0 1 1 1V20a1 1 0 0 1-1 1A17 17 0 0 1 3 4a1 1 0 0 1 1-1h3.5a1 1 0 0 1 1 1 11.4 11.4 0 0 0 .57 3.6 1 1 0 0 1-.25 1Z" fill="var(--rose)"/></svg>
        0271836042
      </div>
      <div class="call__mail">Dana.lumen@mailbay.example</div>
    </div>
    <address class="address">Lumen Nails &amp; Beauty<br>Dana Pirrett<br>Suite 2, 17 Corbel Street<br>Ashmere Bay</address>
    <div class="socials">
      <span class="social"><span class="social__dot"></span>@lumenbeauty</span>
      <span class="social"><span class="social__dot"></span>@lumenbeautyab</span>
    </div>
    <div class="url-pill">www.lumenbeauty.example.nz</div>
  </article>

  <article class="panel cover">
    <svg class="layer" viewBox="0 0 370 740" role="img" aria-label="Portrait photo of a model with long wavy hair and purple manicured nails">
      <defs><linearGradient id="coverPhoto2" x1="0" y1="0" x2="1" y2="1"><stop offset="0" stop-color="#8a6a55"/><stop offset=".5" stop-color="#e2bfae"/><stop offset="1" stop-color="#6b4b45"/></linearGradient></defs>
      <path d="M0 95 Q185 150 370 95 L370 440 Q210 530 0 610 Z" fill="url(#coverPhoto2)"/>
    </svg>
    <svg class="layer" viewBox="0 0 370 740" aria-hidden="true">
      <path d="M0 95 Q185 150 370 95" fill="none" stroke="var(--rose-light)" stroke-width="4"/>
      <path d="M0 606 Q210 526 370 436" fill="none" stroke="var(--blush)" stroke-width="8"/>
      <path d="M0 614 Q210 536 370 446" fill="none" stroke="var(--rose)" stroke-width="4"/>
      <path d="M0 620 Q210 542 370 452 L370 740 L0 740 Z" fill="var(--grey)"/>
    </svg>
    <div class="brand" style="top:20px"><div class="brand__name">Lumen</div><div class="brand__sub">Nails &amp; Beauty</div></div>
    <h2 class="cover__title">Nails &amp; Beauty</h2>
    <div class="url-pill">www.lumenbeauty.example.nz</div>
  </article>
</section>

<section class="sheet sheet--inside">
  <article class="panel">
    <svg class="layer" viewBox="0 0 370 740" aria-hidden="true">
      <rect width="370" height="740" fill="var(--grey)"/>
    </svg>
    <svg class="layer" viewBox="0 0 370 740" role="img" aria-label="Photo of manicured hands resting on pedicured feet">
      <defs><linearGradient id="feetPhoto" x1="0" y1="0" x2="1" y2="0"><stop offset="0" stop-color="#f1dcd3"/><stop offset="1" stop-color="#d9b3a6"/></linearGradient></defs>
      <path d="M0 560 Q185 520 370 580 L370 740 L0 740 Z" fill="url(#feetPhoto)"/>
      <path d="M0 560 Q185 520 370 580" fill="none" stroke="var(--rose-light)" stroke-width="5"/>
    </svg>
    <div class="menu menu--nails">
      <h3 class="menu__title">Nails</h3>
      <div class="menu__group">Manicure</div>
      <div class="row"><span class="row__name">Gel Polish</span><span class="row__dots"></span><span class="row__price">$45</span></div>
      <div class="row"><span class="row__name">Regular Polish</span><span class="row__dots"></span><span class="row__price">$40</span></div>
      <div class="menu__group">Pedicure</div>
      <div class="row"><span class="row__name">Gel Polish</span><span class="row__dots"></span><span class="row__price">$65</span></div>
      <div class="row"><span class="row__name">Regular Polish</span><span class="row__dots"></span><span class="row__price">$60</span></div>
      <div class="menu__group">Luxury Pedicure</div>
      <div class="note">Includes soak, exfoliation, heel scrub &amp; massage</div>
      <div class="row"><span class="row__name">Gel Polish</span><span class="row__dots"></span><span class="row__price">$80</span></div>
      <div class="row"><span class="row__name">Regular Polish</span><span class="row__dots"></span><span class="row__price">$75</span></div>
      <div class="menu__group">Gel Removal &amp; Nail Tidy</div>
      <div class="row"><span class="row__name">Hands or Feet</span><span class="row__dots"></span><span class="row__price">$25</span></div>
      <div class="menu__group">Add On</div>
      <div class="row"><span class="row__name">Gel Removal</span><span class="row__dots"></span><span class="row__price">$5</span></div>
      <div class="row"><span class="row__name">French Tips</span><span class="row__dots"></span><span class="row__price">$5 per set</span></div>
      <div class="row"><span class="row__name">Nail Art, Glitter</span><span class="row__dots"></span><span class="row__price">$10</span></div>
    </div>
  </article>

  <article class="panel">
    <svg class="layer" viewBox="0 0 370 740" aria-hidden="true">
      <path d="M0 14 Q185 0 370 14" fill="none" stroke="var(--rose-light)" stroke-width="4"/>
    </svg>
    <div class="brand brand--ring" style="top:40px"><div class="brand__name">Lumen</div><div class="brand__sub">Nails &amp; Beauty</div></div>
    <div class="menu menu--facials">
      <h3 class="menu__title">Facials</h3>
      <div class="menu__group">Deep Cleansing Facial</div>
      <div class="note">45 minutes. Cleanse, exfoliate and hydrate tired skin.</div>
      <div class="row"><span class="row__name">Per session</span><span class="row__dots"></span><span class="row__price">$75</span></div>
      <div class="menu__group">Therapeutic Facial</div>
      <div class="note">60 minutes. Tailored to your skin's specific needs.</div>
      <div class="row"><span class="row__name">Per session</span><span class="row__dots"></span><span class="row__price">$95</span></div>
      <div class="menu__group">Rejuvenation Facial</div>
      <div class="note">75 minutes. Gentle peel with a renewing mask.</div>
      <div class="row"><span class="row__name">Per session</span><span class="row__dots"></span><span class="row__price">$120</span></div>
      <div class="menu__group">Dermaplaning</div>
      <div class="note">Removes fine hair and dull skin for a smooth finish.</div>
      <div class="row"><span class="row__name">Per session</span><span class="row__dots"></span><span class="row__price">$85</span></div>
      <h3 class="menu__title" style="margin-top:16px">Eyes</h3>
      <div class="row"><span class="row__name">Lash Lift</span><span class="row__dots"></span><span class="row__price">$75</span></div>
      <div class="row"><span class="row__name">Eyebrow Shape</span><span class="row__dots"></span><span class="row__price">$18</span></div>
      <div class="row"><span class="row__name">Eyebrow Tint</span><span class="row__dots"></span><span class="row__price">$15</span></div>
      <div class="row"><span class="row__name">Eyelash Tint</span><span class="row__dots"></span><span class="row__price">$20</span></div>
      <div class="row"><span class="row__name">Eye Trio</span><span class="row__dots"></span><span class="row__price">$45</span></div>
    </div>
  </article>

  <article class="panel">
    <svg class="layer" viewBox="0 0 370 740" role="img" aria-label="Photo of a woman with smooth skin raising her arm">
      <defs><linearGradient id="bodyPhoto" x1="0" y1="0" x2="1" y2="1"><stop offset="0" stop-color="#f4e6e0"/><stop offset=".6" stop-color="#dcb9a8"/><stop offset="1" stop-color="#7a5a4d"/></linearGradient></defs>
      <path d="M0 0 L370 0 L370 320 Q200 410 0 430 Z" fill="url(#bodyPhoto)"/>
    </svg>
    <svg class="layer" viewBox="0 0 370 740" aria-hidden="true">
      <path d="M0 432 Q200 414 370 324" fill="none" stroke="var(--blush)" stroke-width="8"/>
      <path d="M0 440 Q200 422 370 332" fill="none" stroke="var(--rose)" stroke-width="4"/>
      <path d="M0 446 Q200 428 370 338 L370 740 L0 740 Z" fill="var(--grey)"/>
    </svg>
    <div class="menu menu--face">
      <div class="cols">
        <div>
          <h3 class="menu__title">Face</h3>
          <div class="row"><span class="row__name">Lip</span><span class="row__dots"></span><span class="row__price">$15</span></div>
          <div class="row"><span class="row__name">Chin</span><span class="row__dots"></span><span class="row__price">$15</span></div>
          <h3 class="menu__title" style="margin-top:10px">Body</h3>
          <div class="row"><span class="row__name">Under Arm</span><span class="row__dots"></span><span class="row__price">$20</span></div>
          <div class="row"><span class="row__name">1/2 Leg</span><span class="row__dots"></span><span class="row__price">$35</span></div>
          <div class="row"><span class="row__name">3/4 Leg</span><span class="row__dots"></span><span class="row__price">$40</span></div>
          <div class="row"><span class="row__name">Full Leg</span><span class="row__dots"></span><span class="row__price">$50</span></div>
        </div>
        <div style="padding-top:34px">
          <div class="row"><span class="row__name">Basic Bikini</span><span class="row__dots"></span><span class="row__price">$25</span></div>
          <div class="row"><span class="row__name">Ext. Bikini</span><span class="row__dots"></span><span class="row__price">$35</span></div>
          <div class="row"><span class="row__name">Brazilian</span><span class="row__dots"></span><span class="row__price">$60</span></div>
          <div class="row"><span class="row__name">Brazilian (4-6 wk)</span><span class="row__dots"></span><span class="row__price">$50</span></div>
          <div class="row"><span class="row__name">Buttocks</span><span class="row__dots"></span><span class="row__price">$25</span></div>
        </div>
      </div>
    </div>
  </article>
</section>

</body>
</html>
```